Design packaging for dumplings for supermarket shelves

I am looking for packaging design for my new dumplings which are to be put onto gourmet super market shelves. My dumplings are ‘fusion’ and made from very high quality ingredients. My flavours are innovated and produced by me.
The brand is luxe and ‘fun’ combined

Please check out my website for the products, logos and things which i would like it to have.

I do have more photos as well as cartoons of the product but I can’t seem to share them over maker hive. Please enquire and I can see you a file nest link

Target Market(s)

Consumers who want to have a great product to eat at home and not too worried about cost

Industry/Entity Type

Dumplings

Font styles to use
Other font styles liked:
• See font on website www.pocketfold.com

Requirements
Must have
• Photos of the dumplings on the front or to have a window where you can see to dumplings inside the package. Must have space for a nutritional panel as well as a drescription
Nice to have
• It would be nice to see decals which can feature some of the ingredients such as ‘Wagyu Beef’ and ‘Victorian Berkshire Pork’

```html
<!DOCTYPE html>
<html lang="en">
<head>
<meta charset="utf-8">
<title>Plump Pockets – Wagyu &amp; Kimchi Dumplings Label</title>
<link rel="stylesheet" href="https://fonts.googleapis.com/css2?family=Bebas+Neue&display=swap">
<style>
  :root {
    --page-bg: #e4e5e7;
    --cream: #fff5df;
    --peach: #fdd3ae;
    --brand-red: #d64545;
    --dumpling-red: #ee6b5e;
    --dumpling-soft: #f4a08f;
    --text-light: #fff8ec;
  }
  * { margin: 0; padding: 0; box-sizing: border-box; }
  html, body {
    width: 1200px;
    height: 1080px;
    overflow: hidden;
    background: var(--page-bg);
  }
  .canvas {
    position: relative;
    width: 1200px;
    height: 1080px;
  }
  .label {
    position: absolute;
    left: 193px;
    top: 40px;
    width: 814px;
    height: 1000px;
    overflow: hidden;
    font-family: "Bebas Neue", sans-serif;
  }
  .label-backdrop {
    position: absolute;
    inset: 0;
    background: radial-gradient(circle at 50% 62%, #fffdf6 0%, var(--cream) 28%, #fde6cc 60%, var(--peach) 100%);
  }
  .brand {
    position: absolute;
    left: 0;
    right: 0;
    top: 206px;
    display: flex;
    justify-content: center;
    align-items: center;
    gap: 12px;
  }
  .brand-dot {
    width: 22px;
    height: 22px;
    border-radius: 50%;
    background: var(--brand-red);
  }
  .brand-name {
    font-size: 52px;
    line-height: 1;
    letter-spacing: 1px;
    color: var(--brand-red);
  }
  .flavour-title {
    position: absolute;
    left: 0;
    right: 0;
    top: 300px;
    text-align: center;
    font-size: 146px;
    line-height: 1;
    letter-spacing: 1px;
    color: var(--brand-red);
  }
  .product-art {
    position: absolute;
    left: 154px;
    top: 452px;
    width: 506px;
    height: 322px;
    border-radius: 40px;
    background: radial-gradient(ellipse at 50% 55%, var(--dumpling-red) 0%, var(--dumpling-soft) 55%, rgba(253, 211, 174, 0) 100%);
  }
  .claim-pill {
    position: absolute;
    left: 38px;
    top: 849px;
    width: 738px;
    height: 80px;
    border-radius: 26px;
    background: var(--brand-red);
    display: flex;
    align-items: center;
    justify-content: center;
  }
  .claim-text {
    font-size: 45px;
    line-height: 1;
    padding-top: 4px;
    color: var(--text-light);
    letter-spacing: 0.5px;
  }
</style>
</head>
<body>
  <main class="canvas">
    <section class="label">
      <div class="label-backdrop" role="img" aria-label="Cream and peach sunburst rays radiating from behind the dumpling"></div>

      <div class="brand">
        <span class="brand-dot"></span>
        <span class="brand-name">PLUMP POCKETS</span>
      </div>

      <h1 class="flavour-title">WAGYU &amp; KIMCHI</h1>

      <div class="product-art" role="img" aria-label="Cartoon illustration of a red kimchi dumpling mascot"></div>

      <div class="claim-pill">
        <p class="claim-text">MADE WITH REAL WAGYU BEEF &amp; KIMCHI!</p>
      </div>
    </section>
  </main>
</body>
</html>
```